Coupons App Design Project

We have a simple coupons app with few screens and actions:
1. Very simple login screen (with chatterloop and findwell+)
2. Very simple business search page
3. Very simple business search results(each result contains logo icon, business name and delete icon)
4. business list (every row contains logo icon, business name and delete icon)
5. coupons list (each item contains image, title, subtitle, description, expiration time, status graphics (valid, expired, redeemed), delete icon
6. coupon view (image, title, subtitle, description, barcode etc.)
7. custom confirmation dialog(title, buttons, background, text)
8. "scan to subscribe" page (merchant name, merchant number, background image, text, barcode to scan etc.)
9. simple menu
10. splash screen

all graphics should be vector graphics so we can use it to different resolutions including for printing
Updates

Hi all, We've increased the project's budget by 25%. Thanks

Hi all,

We've decided to change the project from refundable to committed payment.
FYI

Hi All,

Thank you for your time and efforts, we really appreciate it.However we've eliminated most of the offered designs we've received becausethey didn't fit our desired look and feel.

Please download our look and feel file from our uploaded files -we've put there some examples of other apps that we like.

Thanks

Target Market(s)

shoppers all over the world

Industry/Entity Type

Business

Requirements
Must have
• Please take a look at the attached file "look & feel.jpg" for some nice screen shots taken from apps that we like

Should not have
• *****************************************************************************************
The attached files are only for demonstration purpose and needs descriptions so please don't send us design based on these screenshots.
*****************************************************************************************

```html
<!DOCTYPE html>
<html lang="en">
<head>
<meta charset="utf-8">
<title>Coupons App – Business List</title>
<link href="https://fonts.googleapis.com/css2?family=Lato:wght@400;700&family=Roboto:wght@400&display=swap" rel="stylesheet">
<style>
  :root {
    --status-bg: #000000;
    --status-fg: #ffffff;
    --bar-top: #4aa9f3;
    --bar-bottom: #0b6ad6;
    --bar-fg: #ffffff;
    --page-bg: #1d1d1d;
    --strip-bg: #cfcfcf;
    --card-bg: #f3f3f3;
    --row-line: #d2d2d2;
    --title: #2b2b2b;
    --body: #9b9b9b;
    --placeholder: #a5a5a5;
    --tile-bg: #dedede;
    --tile-fg: #4a4a4a;
    --icon: #333333;
  }
  * { box-sizing: border-box; margin: 0; padding: 0; }
  html, body { width: 674px; height: 1200px; overflow: hidden; background: var(--page-bg); }
  .screen { position: relative; width: 674px; height: 1200px; overflow: hidden; font-family: "Lato", sans-serif;
    background: repeating-linear-gradient(0deg, #1b1b1b 0 2px, #222 2px 4px); }

  .status-bar { position: absolute; inset: 0 0 auto 0; height: 46px; background: var(--status-bg);
    color: var(--status-fg); font-family: "Roboto", sans-serif; }
  .status-bar .usb { position: absolute; left: 24px; top: 6px; }
  .status-bar .right { position: absolute; right: 14px; top: 0; height: 46px; display: flex; align-items: center; gap: 10px; }
  .status-bar .percent { font-size: 25px; }
  .status-bar .clock { font-size: 29px; margin-left: 8px; }

  .app-bar { position: absolute; top: 46px; left: 0; width: 674px; height: 83px;
    background: linear-gradient(var(--bar-top), var(--bar-bottom)); color: var(--bar-fg);
    display: flex; align-items: center; border-bottom: 1px solid #0a58b3; }
  .app-bar .title { font-size: 41px; margin-left: 6px; letter-spacing: -0.3px; }
  .app-bar .back { font-size: 34px; margin-left: 4px; font-weight: 700; }
  .app-bar .search { position: absolute; left: 570px; top: 20px; }
  .app-bar .menu { position: absolute; left: 642px; top: 22px; }

  .tab-strip { position: absolute; top: 129px; left: 0; width: 674px; height: 17px; background: var(--strip-bg); }
  .tab-strip::after { content: ""; position: absolute; left: 337px; top: 0; width: 1px; height: 17px; background: #555; }

  .search-popover { position: absolute; left: 17px; top: 146px; width: 639px; height: 67px; background: #fff;
    border-radius: 6px; box-shadow: 0 2px 4px rgba(0,0,0,.4); display: flex; align-items: center; padding-left: 32px;
    color: var(--placeholder); font-size: 16px; }
  .search-popover::before { content: ""; position: absolute; left: 584px; top: -18px; border-style: solid;
    border-color: transparent transparent #fff transparent; border-width: 0 11px 18px 11px; }

  .business-list { position: absolute; left: 4px; top: 230px; width: 666px; background: var(--card-bg);
    border-radius: 5px; list-style: none; padding-top: 3px; }
  .business-row { position: relative; height: 129px; border-bottom: 1px solid var(--row-line); }
  .business-tile { position: absolute; left: 13px; top: 13px; width: 102px; height: 102px; background: var(--tile-bg);
    border-radius: 3px; display: flex; align-items: center; justify-content: center;
    color: var(--tile-fg); font-size: 18px; font-weight: 400; }
  .business-name { position: absolute; left: 131px; top: 14px; font-size: 28px; font-weight: 400; color: var(--title); }
  .business-desc { position: absolute; left: 131px; top: 58px; width: 466px; font-size: 17.5px; line-height: 24px; color: var(--body); }
  .delete { position: absolute; left: 630px; top: 88px; }
</style>
</head>
<body>
<div class="screen">
  <div class="status-bar">
    <svg class="usb" width="22" height="32" viewBox="0 0 22 32" fill="#ccc"><path d="M11 0l4 6h-3v16l5-4v-4h-2v-4h5v4h-1v5l-7 6v3a3 3 0 1 1-2 0v-6l-6-5v-3a2.5 2.5 0 1 1 2 0v2l4 3V6H7z"/></svg>
    <div class="right">
      <svg width="34" height="34" viewBox="0 0 34 34" fill="none" stroke="#fff" stroke-width="3"><circle cx="17" cy="19" r="12"/><path d="M17 12v7h6M4 7l6-5M30 7l-6-5"/></svg>
      <svg width="34" height="30" viewBox="0 0 34 30" fill="#fff"><text x="0" y="12" font-size="12" font-family="Roboto, sans-serif" font-weight="700">H</text><rect x="8" y="22" width="5" height="8"/><rect x="15" y="16" width="5" height="14"/><rect x="22" y="9" width="5" height="21" fill="#888"/><rect x="29" y="2" width="5" height="28" fill="#888"/></svg>
      <span class="percent">54%</span>
      <svg width="36" height="24" viewBox="0 0 36 24" fill="none" stroke="#fff" stroke-width="2"><rect x="1" y="3" width="30" height="18"/><rect x="31" y="8" width="4" height="8" fill="#fff"/><rect x="4" y="6" width="16" height="12" fill="#8cc63f" stroke="none"/><path d="M18 5l-6 8h6l-4 7" stroke="#000"/></svg>
      <span class="clock">12:08 pm</span>
    </div>
  </div>

  <header class="app-bar">
    <span class="back">‹</span><span class="title">App name</span>
    <svg class="search" width="40" height="42" viewBox="0 0 40 42" fill="none" stroke="#fff" stroke-width="4"><circle cx="15" cy="15" r="11"/><path d="M23 24l13 14" stroke-width="7" stroke-linecap="round"/></svg>
    <svg class="menu" width="14" height="38" viewBox="0 0 14 38" fill="#fff"><rect x="2" y="0" width="9" height="9"/><rect x="2" y="14" width="9" height="9"/><rect x="2" y="28" width="9" height="9"/></svg>
  </header>

  <div class="tab-strip"></div>
  <div class="search-popover">You can search here</div>

  <ul class="business-list">
    <li class="business-row">
      <div class="business-tile">Tovari</div>
      <h2 class="business-name">Lorem Ipsum</h2>
      <p class="business-desc">Each slider illustrates characteristics of the customer's brand and the style your design should communicate.</p>
      <svg class="delete" width="26" height="28" viewBox="0 0 26 28" fill="none" stroke="#333" stroke-width="2.6"><path d="M2 6h22M9 6V2h8v4M5 6v20h16V6M10 11v11M16 11v11"/></svg>
    </li>
    <li class="business-row">
      <div class="business-tile">Tovari</div>
      <h2 class="business-name">Lorem Ipsum</h2>
      <p class="business-desc">Each slider illustrates characteristics of the customer's brand and the style your design should communicate.</p>
      <svg class="delete" width="26" height="28" viewBox="0 0 26 28" fill="none" stroke="#333" stroke-width="2.6"><path d="M2 6h22M9 6V2h8v4M5 6v20h16V6M10 11v11M16 11v11"/></svg>
    </li>
    <li class="business-row">
      <div class="business-tile">Tovari</div>
      <h2 class="business-name">Lorem Ipsum</h2>
      <p class="business-desc">Each slider illustrates characteristics of the customer's brand and the style your design should communicate.</p>
      <svg class="delete" width="26" height="28" viewBox="0 0 26 28" fill="none" stroke="#333" stroke-width="2.6"><path d="M2 6h22M9 6V2h8v4M5 6v20h16V6M10 11v11M16 11v11"/></svg>
    </li>
    <li class="business-row">
      <div class="business-tile">Tovari</div>
      <h2 class="business-name">Lorem Ipsum</h2>
      <p class="business-desc">Each slider illustrates characteristics of the customer's brand and the style your design should communicate.</p>
      <svg class="delete" width="26" height="28" viewBox="0 0 26 28" fill="none" stroke="#333" stroke-width="2.6"><path d="M2 6h22M9 6V2h8v4M5 6v20h16V6M10 11v11M16 11v11"/></svg>
    </li>
    <li class="business-row">
      <div class="business-tile">Tovari</div>
      <h2 class="business-name">Lorem Ipsum</h2>
      <p class="business-desc">Each slider illustrates characteristics of the customer's brand and the style your design should communicate.</p>
      <svg class="delete" width="26" height="28" viewBox="0 0 26 28" fill="none" stroke="#333" stroke-width="2.6"><path d="M2 6h22M9 6V2h8v4M5 6v20h16V6M10 11v11M16 11v11"/></svg>
    </li>
    <li class="business-row">
      <div class="business-tile">Tovari</div>
      <h2 class="business-name">Lorem Ipsum</h2>
      <p class="business-desc">Each slider illustrates characteristics of the customer's brand and the style your design should communicate.</p>
      <svg class="delete" width="26" height="28" viewBox="0 0 26 28" fill="none" stroke="#333" stroke-width="2.6"><path d="M2 6h22M9 6V2h8v4M5 6v20h16V6M10 11v11M16 11v11"/></svg>
    </li>
    <li class="business-row">
      <div class="business-tile">Tovari</div>
      <h2 class="business-name">Lorem Ipsum</h2>
      <p class="business-desc">Each slider illustrates characteristics of the customer's brand and the style your design should communicate.</p>
      <svg class="delete" width="26" height="28" viewBox="0 0 26 28" fill="none" stroke="#333" stroke-width="2.6"><path d="M2 6h22M9 6V2h8v4M5 6v20h16V6M10 11v11M16 11v11"/></svg>
    </li>
    <li class="business-row">
      <div class="business-tile">Tovari</div>
      <h2 class="business-name">Lorem Ipsum</h2>
      <p class="business-desc">Each slider illustrates characteristics of the customer's brand and the style your design should communicate.</p>
      <svg class="delete" width="26" height="28" viewBox="0 0 26 28" fill="none" stroke="#333" stroke-width="2.6"><path d="M2 6h22M9 6V2h8v4M5 6v20h16V6M10 11v11M16 11v11"/></svg>
    </li>
  </ul>
</div>
</body>
</html>
```